Quantum Computing Poster

Design some retro futuristic design posters on quantum computing. Need these posters for office prints. See reference image.

```html
<!DOCTYPE html>
<html lang="en">
<head>
<meta charset="utf-8">
<title>Quantum Computing Poster</title>
<link rel="stylesheet" href="https://fonts.googleapis.com/css2?family=Open+Sans:wght@400&family=Stardos+Stencil:wght@700&display=swap">
<style>
  :root {
    --ink: #222731;
    --paper: #e6e7e8;
    --teal: #4f8a8a;
    --gold: #fdd56b;
    --lilac: #ae78b6;
    --violet: #7b2a8f;
    --magenta: #c0178b;
    --pink: #d870ac;
    --grey: #c9cbcd;
  }
  html, body {
    margin: 0;
    padding: 0;
    width: 855px;
    height: 1200px;
    overflow: hidden;
    background: var(--ink);
  }
  .poster {
    display: block;
    width: 855px;
    height: 1200px;
  }
  .title {
    font-family: "Stardos Stencil", serif;
    font-weight: 700;
  }
  .title-face { fill: var(--paper); }
  .title-shadow { fill: var(--teal); }
  .code-line {
    font-family: "Stardos Stencil", serif;
    font-weight: 700;
    fill: #ffffff;
  }
  .small-print {
    font-family: "Open Sans", sans-serif;
    font-weight: 400;
    fill: var(--gold);
  }
  .accent-triangle { fill: var(--gold); }
  .prism { fill: url(#prismFill); }
</style>
</head>
<body>
<svg class="poster" viewBox="0 0 1624 2296" preserveAspectRatio="none" xmlns="http://www.w3.org/2000/svg">
  <defs>
    <linearGradient id="frameStroke" x1="0" y1="0" x2="1" y2="0">
      <stop offset="0" stop-color="#b07fbb"/>
      <stop offset="1" stop-color="#7a2a8c"/>
    </linearGradient>
    <linearGradient id="floorFill" x1="0" y1="0" x2="1" y2="0">
      <stop offset="0" stop-color="#b27fbd"/>
      <stop offset="0.45" stop-color="#8c3d9b"/>
      <stop offset="1" stop-color="#7a2a8f"/>
    </linearGradient>
    <linearGradient id="largeSphere" x1="0" y1="0" x2="1" y2="0">
      <stop offset="0" stop-color="#b07ab8"/>
      <stop offset="0.5" stop-color="#8a3b9a"/>
      <stop offset="1" stop-color="#742a8d"/>
    </linearGradient>
    <linearGradient id="pinkSphere" x1="0" y1="0" x2="1" y2="0">
      <stop offset="0" stop-color="#da74ad"/>
      <stop offset="0.45" stop-color="#c0178b"/>
      <stop offset="1" stop-color="#b41f8e"/>
    </linearGradient>
    <linearGradient id="prismFill" x1="0" y1="0" x2="1" y2="0">
      <stop offset="0" stop-color="#7d2f92"/>
      <stop offset="0.5" stop-color="#b584c0"/>
      <stop offset="0.5" stop-color="#a91d90"/>
      <stop offset="0.8" stop-color="#c4198a"/>
      <stop offset="1" stop-color="#d868aa"/>
    </linearGradient>
    <linearGradient id="illustrationTone" x1="0" y1="0" x2="1" y2="1">
      <stop offset="0" stop-color="#d3d5d6" stop-opacity="0.22"/>
      <stop offset="1" stop-color="#d3d5d6" stop-opacity="0.08"/>
    </linearGradient>
    <pattern id="pinstripe" width="9" height="20" patternUnits="userSpaceOnUse">
      <rect x="0" y="0" width="1.5" height="20" fill="#ffffff" opacity="0.09"/>
    </pattern>
    <pattern id="dotGridGrey" width="13.5" height="14.5" patternUnits="userSpaceOnUse">
      <rect x="0" y="0" width="9" height="9" fill="var(--grey)"/>
    </pattern>
    <pattern id="dotGridPink" width="8" height="9" patternUnits="userSpaceOnUse">
      <rect x="0" y="0" width="5" height="5" fill="#d0258f"/>
    </pattern>
  </defs>

  <!-- backdrop -->
  <rect class="backdrop" width="1624" height="2296" fill="var(--ink)"/>
  <rect class="backdrop-stripes" x="72" y="100" width="1481" height="2066" fill="url(#pinstripe)"/>

  <!-- diagonal floor -->
  <polygon class="floor-edge" points="0,2262 1624,1096 1624,1128 0,2296" fill="var(--teal)"/>
  <polygon class="floor" points="0,2296 1624,1128 1624,2296" fill="url(#floorFill)"/>
  <polygon class="floor-stripes" points="0,2296 1624,1128 1624,2296" fill="url(#pinstripe)"/>

  <!-- frame -->
  <rect class="frame" x="72" y="100" width="1481" height="2066" fill="none" stroke="url(#frameStroke)" stroke-width="14"/>

  <!-- spheres -->
  <circle class="sphere-large" cx="1015" cy="622" r="350" fill="url(#largeSphere)" stroke="var(--teal)" stroke-width="5"/>
  <circle class="sphere-pink" cx="1245" cy="388" r="233" fill="url(#pinkSphere)" stroke="var(--teal)" stroke-width="5"/>

  <!-- illustration area -->
  <rect class="illustration-area" x="218" y="432" width="1142" height="838" rx="220"
        fill="url(#illustrationTone)" role="img"
        aria-label="Line illustration of a computer mouse with a looping cable"/>

  <!-- dot grids -->
  <rect class="grid-grey" x="1441" y="647" width="108" height="143" fill="url(#dotGridGrey)"/>
  <rect class="grid-pink" x="333" y="2128" width="88" height="144" fill="url(#dotGridPink)"/>

  <!-- prisms -->
  <polygon class="prism" points="337,422 254,565 420,565"/>
  <polygon class="prism" points="693,220 670,260 717,260"/>
  <polygon class="prism" points="515,806 468,888 563,888"/>
  <polygon class="prism" points="1399,940 1316,1083 1482,1083"/>
  <polygon class="prism" points="218,1513 194,1553 242,1553"/>
  <polygon class="prism" points="520,1528 434,1797 607,1797"/>
  <polygon class="prism" points="1001,1513 955,1593 1048,1593"/>
  <polygon class="prism" points="1508,1458 1490,1497 1525,1497"/>
  <polygon class="prism" points="835,1876 812,1917 859,1917"/>
  <polygon class="prism" points="1277,1663 1157,2040 1398,2040"/>

  <!-- gold accents -->
  <polygon class="accent-triangle" points="990,133 967,173 1013,173"/>
  <polygon class="accent-triangle" points="562,1798 539,1838 585,1838"/>
  <polygon class="accent-triangle" points="1516,2127 1474,2205 1557,2205"/>

  <!-- headline -->
  <g class="title">
    <text class="title-shadow" x="162" y="1374" font-size="218" textLength="1302" lengthAdjust="spacingAndGlyphs">QUANTUM</text>
    <text class="title-face" x="168" y="1368" font-size="218" textLength="1302" lengthAdjust="spacingAndGlyphs">QUANTUM</text>
    <text class="title-shadow" x="296" y="1523" font-size="162" textLength="1128" lengthAdjust="spacingAndGlyphs">COMPUTING</text>
    <text class="title-face" x="302" y="1517" font-size="162" textLength="1128" lengthAdjust="spacingAndGlyphs">COMPUTING</text>
  </g>

  <text class="code-line" x="622" y="1593" font-size="38" textLength="282" lengthAdjust="spacingAndGlyphs">4765598CUPet762</text>

  <!-- small print -->
  <text class="small-print" transform="translate(161 410) rotate(-90)" font-size="19" textLength="145" lengthAdjust="spacingAndGlyphs">4763598CUPet762</text>
  <text class="small-print" x="148" y="2084" font-size="22" textLength="510" lengthAdjust="spacingAndGlyphs">WWW.QUBITHORIZONLAB.FUTURE//MELLENIAL</text>
  <text class="small-print" transform="translate(1531 1955) rotate(-90)" font-size="30" textLength="350" lengthAdjust="spacingAndGlyphs">qubitLab.netrrsr.orbit</text>
</svg>
</body>
</html>
```